Harbor Nightclub

Nightclub flyer., digital single sided, for KV and PX. I included samples of some previous flyers we've used. Sample Info:
HARBOR
FRIDAYS
FRI MAY 1 2020
DJ VORTAN (club floor)
DJ RUZO & DJ TAV (residents on the lounge floor)
4217 Marlow Avenue Sacramento
www.harborvenuehall.example for list/VIP inquiries

Target Market(s)

Upscale top 40 crowd but want some cool and artsy like the examples included.

Font styles to use
Sans Serif

Requirements
Must have
• Harbor Logo
Nice to have
• Would be nice if the flyer can be incorporated later with DJ photos (sometimes we will add dj photos to pixagram etc). Would like a big city type of feel.
Should not have
• Nothing too sexual.

```html
<!DOCTYPE html>
<html lang="en">
<head>
<meta charset="utf-8">
<title>Harbor Fridays</title>
<link href="https://fonts.googleapis.com/css2?family=Montserrat:wght@400;500;600&family=Archivo+Narrow:wght@400;500&display=swap" rel="stylesheet">
<style>
  :root {
    --night: #07070f;
    --navy: #141440;
    --white: #ffffff;
    --ink: #1a1420;
    --band-edge: #e63c6e;
    --rule-red: #d4182c;
  }
  html, body {
    margin: 0;
    padding: 0;
    width: 927px;
    height: 1200px;
    overflow: hidden;
    background: var(--night);
  }
  .flyer {
    position: relative;
    width: 927px;
    height: 1200px;
    overflow: hidden;
    background: radial-gradient(ellipse at 50% 110%, #2a2a8a 0%, var(--navy) 45%, var(--night) 80%);
    color: var(--white);
    font-family: "Montserrat", sans-serif;
  }
  .dj-artwork {
    position: absolute;
    left: 0;
    top: 545px;
    width: 927px;
    height: 655px;
    background:
      radial-gradient(ellipse 38% 30% at 50% 22%, rgba(190, 60, 200, 0.55), transparent 70%),
      radial-gradient(ellipse 70% 60% at 50% 55%, rgba(70, 60, 200, 0.7), transparent 75%),
      linear-gradient(180deg, transparent 0%, rgba(20, 18, 60, 0.4) 100%);
  }
  .event-name {
    position: absolute;
    left: 0;
    top: 60px;
    width: 927px;
    height: 200px;
  }
  .event-name text {
    font-family: "Montserrat", sans-serif;
    font-weight: 400;
    fill: var(--white);
  }
  .date-band {
    position: absolute;
    left: 100px;
    top: 310px;
    width: 727px;
    height: 70px;
    background: linear-gradient(90deg, rgba(255,255,255,0) 0%, #e9d4dc 18%, #e8c8d8 45%, #b49ad8 75%, rgba(120,90,200,0) 100%);
    border-top: 2px solid var(--band-edge);
  }
  .date-text {
    position: absolute;
    left: 0;
    top: 316px;
    width: 927px;
    text-align: center;
    font-family: "Archivo Narrow", sans-serif;
    font-size: 58px;
    line-height: 64px;
    color: var(--ink);
  }
  .headliners {
    position: absolute;
    left: 0;
    top: 428px;
    width: 927px;
    display: flex;
    justify-content: center;
    align-items: center;
    gap: 14px;
    font-size: 62px;
    font-weight: 600;
    letter-spacing: 4px;
    line-height: 72px;
  }
  .headliners .amp {
    font-size: 38px;
    letter-spacing: 0;
  }
  .headliners .rule {
    width: 46px;
    height: 2px;
    background: var(--rule-red);
  }
  .lounge-note {
    position: absolute;
    left: 0;
    top: 507px;
    width: 927px;
    text-align: center;
    font-family: "Archivo Narrow", sans-serif;
    font-size: 31px;
    line-height: 36px;
  }
  .club-floor {
    position: absolute;
    left: 44px;
    top: 928px;
    font-family: "Archivo Narrow", sans-serif;
  }
  .club-floor .name { font-size: 33px; line-height: 38px; }
  .club-floor .floor { font-family: "Montserrat", sans-serif; font-size: 20px; letter-spacing: 3px; line-height: 26px; }
  .venue {
    position: absolute;
    right: 46px;
    top: 928px;
    text-align: center;
    font-family: "Archivo Narrow", sans-serif;
  }
  .venue .street { font-size: 33px; line-height: 38px; }
  .venue .city { font-family: "Montserrat", sans-serif; font-size: 20px; letter-spacing: 3px; line-height: 26px; }
  .website {
    position: absolute;
    left: 0;
    top: 1126px;
    width: 927px;
    text-align: center;
    font-size: 21px;
    letter-spacing: 6px;
    line-height: 28px;
  }
  .inquiries {
    position: absolute;
    left: 0;
    top: 1162px;
    width: 927px;
    text-align: center;
    font-size: 15px;
    letter-spacing: 1.5px;
    line-height: 20px;
  }
</style>
</head>
<body>
<main class="flyer">
  <div class="dj-artwork" role="img" aria-label="Silhouette of a DJ in headphones with arms spread over turntables, on a purple halftone dot backdrop"></div>

  <svg class="event-name" viewBox="0 0 927 200" aria-label="Harbor Fridays">
    <text x="463" y="116" text-anchor="middle" font-size="125" textLength="598" lengthAdjust="spacingAndGlyphs">HARBOR</text>
    <text x="480" y="186" text-anchor="middle" font-size="80" textLength="370" lengthAdjust="spacingAndGlyphs">FRIDAYS</text>
  </svg>

  <div class="date-band"></div>
  <div class="date-text">FRI - MAY - 01 - 2020</div>

  <div class="headliners">
    <span>DJ RUZO</span>
    <span class="rule"></span>
    <span class="amp">&amp;</span>
    <span class="rule"></span>
    <span>DJ TAV</span>
  </div>
  <div class="lounge-note">(RESIDENTS ON THE LOUNGE FLOOR)</div>

  <div class="club-floor">
    <div class="name">DJ VORTAN</div>
    <div class="floor">(CLUB FLOOR)</div>
  </div>

  <div class="venue">
    <div class="street">4217 Marlow Avenue</div>
    <div class="city">SACRAMENTO</div>
  </div>

  <div class="website">www.harborvenuehall.example</div>
  <div class="inquiries">FOR LIST / VIP INQUIRIES</div>
</main>
</body>
</html>
```